Business is called "Pelton Ledger". Accounting and tax services.

I need a flyer for my new business "Pelton Ledger". I am an individual accountant working for himself on the Sunshine Coast in Queensland Australia. I would like to see designs that communicate reliability and trust. I believe my point of difference is that I am always available to my clients and I will cap my number of clients to ensure I can service them properly. Accountants in general seem to have a bad reputation for not responding to clients in a timely fashion, whether by email or phone. This is where I intend to differentiate myself. I have included my business card for ideas on colour and for contact information. I have also included some logo's that should go on the flyer. With the QLA logo, the words "Pelton Ledger is a QLA Business" needs to be written either above, below or to the right hand side (as per the business card).

Target Market(s)

Small business owners and individuals requiring taxation and financials

Industry/Entity Type

Public Accounting

Font styles to use
Serif

Requirements
Must have
• Supplied logo's, accounting style pictures etc
Services: Small Business Taxation
Company & Trust Tax Returns
Rental Property Returns
Capital Gains Tax
Individual Tax Returns
BAS and IAS lodgements
Nice to have
• Needs to convey a sense of being reliable and responds to clients quickly.
Should not have
• My name

```html
<!DOCTYPE html>
<html lang="en">
<head>
<meta charset="utf-8">
<title>Pelton Ledger – Flyer</title>
<link href="https://fonts.googleapis.com/css2?family=Montserrat:wght@500&family=Oswald:wght@300;400&family=Open+Sans:wght@300;400&display=swap" rel="stylesheet">
<style>
  :root{
    --green-light:#29b995;
    --green-mid:#22a687;
    --green-dark:#18705b;
    --green-text:#1a6b55;
    --blue:#005ea6;
    --yellow:#ffd500;
    --sky:#17b5e8;
    --lime:#b7d13a;
    --ink:#333;
    --grey:#7a7a7a;
    --paper:#fff;
    --frame:#2a2a2a;
  }
  *{margin:0;padding:0;box-sizing:border-box}
  html,body{width:1179px;height:1200px;overflow:hidden;background:var(--paper)}
  .canvas{position:relative;width:1179px;height:1200px;border:1px solid var(--frame);background:var(--paper)}
  .flyer{position:absolute;left:329px;top:233px;width:520px;height:733px;background:var(--paper);
    border:1px solid var(--frame);box-shadow:0 4px 22px rgba(0,0,0,.22);overflow:hidden}
  .header{position:absolute;left:0;top:0;width:100%;height:225px;
    background:linear-gradient(160deg,var(--green-light) 0%,var(--green-mid) 100%)}
  .brand-mark{position:absolute;left:209px;top:38px;width:102px;height:102px;border:2.5px solid #fff;border-radius:50%}
  .brand-name{position:absolute;left:0;top:154px;width:100%;text-align:center;color:#fff;
    font-family:"Montserrat",sans-serif;font-weight:500;font-size:29px;letter-spacing:12px;padding-left:12px}
  .membership{position:absolute;left:0;top:225px;width:100%;height:81px;display:flex}
  .membership-statement{width:333px;background:var(--green-dark);color:#fff;display:flex;align-items:center;justify-content:center;
    font-family:"Oswald",sans-serif;font-weight:300;font-size:24px;letter-spacing:-.3px;text-transform:uppercase}
  .membership-name{width:116px;background:var(--blue);color:var(--yellow);display:flex;align-items:center;justify-content:center;
    font-family:"Oswald",sans-serif;font-weight:400;font-size:36px}
  .membership-seal{flex:1;background:var(--yellow);display:flex;align-items:center;justify-content:center}
  .membership-seal span{width:34px;height:34px;border-radius:50%;background:var(--blue)}
  .services{position:absolute;left:108px;top:380px;list-style:none}
  .services li{position:relative;height:25.5px;line-height:25.5px;padding-left:34px;
    font-family:"Open Sans",sans-serif;font-weight:300;font-size:20px;color:var(--ink);white-space:nowrap}
  .services li::before{content:"";position:absolute;left:0;top:3px;width:20px;height:20px;background:var(--green-light)}
  .registration{position:absolute;left:43px;top:614px;width:60px;text-align:center}
  .registration-badge{width:58px;height:58px;margin:0 auto;border-radius:50%;border:1.5px solid #222;display:flex;align-items:center;justify-content:center}
  .registration-badge span{width:28px;height:28px;border-radius:50%;background:var(--lime)}
  .registration-number{margin-top:5px;font-family:Arial,sans-serif;font-size:7px;line-height:9px;color:#111}
  .contact{position:absolute;left:0;top:610px;width:520px;text-align:center;font-family:"Open Sans",sans-serif;font-weight:300}
  .contact-phone{font-size:27px;color:var(--green-text);line-height:38px;letter-spacing:-.5px}
  .contact-line{font-size:19.5px;color:var(--grey);line-height:24px}
  .software-partner{position:absolute;left:425px;top:629px;width:56px;height:56px;border-radius:50%;background:var(--sky)}
</style>
</head>
<body>
<div class="canvas">
  <article class="flyer">
    <header class="header">
      <div class="brand-mark"></div>
      <div class="brand-name">PELTON LEDGER</div>
    </header>
    <div class="membership">
      <div class="membership-statement">Pelton Ledger is a QLA Business</div>
      <div class="membership-name">QLA</div>
      <div class="membership-seal"><span></span></div>
    </div>
    <ul class="services">
      <li>Small Business Taxation</li>
      <li>Company &amp; Trust Tax Returns</li>
      <li>Rental Property Returns</li>
      <li>Capital Gains Tax</li>
      <li>Individual Tax Returns</li>
      <li>BAS and IAS lodgements</li>
    </ul>
    <div class="registration">
      <div class="registration-badge"><span></span></div>
      <p class="registration-number">Tax agent<br>48210937</p>
    </div>
    <div class="contact">
      <p class="contact-phone">0412 583 906</p>
      <p class="contact-line">www.peltonledger.com.au</p>
      <p class="contact-line">hello@peltonledger.com.au</p>
    </div>
    <div class="software-partner"></div>
  </article>
</div>
</body>
</html>
```